Letterhead and Stationary for Construction Company

Lumen Forge needs modern Letterhead, Envelopes and Notepad designs.

Industry/Entity Type

Construction

Colors
f78f20
34a7d8
ffffff

Requirements
Must have
• Modern looking design.

```html
<!DOCTYPE html>
<html lang="en">
<head>
<meta charset="utf-8">
<title>Lumen Forge Stationery</title>
<link href="https://fonts.googleapis.com/css2?family=Open+Sans:wght@400;600;700&display=swap" rel="stylesheet">
<style>
  :root{
    --orange:#f07a22;
    --blue:#1f73be;
    --paper:#ffffff;
    --backdrop:#e6e6e6;
    --ink:#6b6b6b;
    --rule:#d6d6d6;
    --edge:#d0d0d0;
  }
  *{box-sizing:border-box;margin:0;padding:0}
  html,body{width:1200px;height:630px;overflow:hidden}
  body{background:var(--backdrop);font-family:"Open Sans",Arial,sans-serif;color:var(--ink);position:relative}
  .sheet{position:absolute;background:var(--paper);border:1px solid var(--edge)}
  .band{position:absolute;left:0;right:0;bottom:0;height:6px;
    background:linear-gradient(115deg,var(--orange) 49.4%,var(--paper) 49.4% 50%,var(--blue) 50%)}
  .brand{position:absolute;display:flex;align-items:center;gap:5px;color:var(--blue);font-weight:700;letter-spacing:-.2px}
  .brand .dot{border-radius:50%;background:var(--orange);flex:none}
  .brand .name{display:flex;flex-direction:column;line-height:.95}
  .brand-lg{font-size:17px}
  .brand-lg .dot{width:22px;height:22px}
  .brand-md{font-size:11px}
  .brand-md .dot{width:15px;height:15px}
  .brand-sm{font-size:10px;gap:4px}
  .brand-sm .dot{width:12px;height:12px}
  .brand-white{color:var(--paper)}
  .contact{position:absolute;font-size:6.5px;line-height:1.4;white-space:nowrap}
  .contact .row{display:flex;align-items:center;gap:4px}
  .contact .row svg{width:6px;height:6px;flex:none}
  .letterhead{left:35px;top:40px;width:409px;height:538px}
  .letterhead .brand{left:22px;top:28px}
  .letterhead .contact{left:304px;top:22px}
  .card-front{left:472px;top:62px;width:144px;height:82px}
  .card-front .brand{left:10px;top:26px}
  .card-front .divider{position:absolute;left:80px;top:18px;width:1px;height:34px;background:var(--orange)}
  .card-front .person{position:absolute;left:85px;top:18px;font-size:4px;line-height:1.3;white-space:nowrap}
  .card-front .person .who{color:var(--blue);font-weight:700;font-size:6px}
  .card-front .band{height:4px}
  .card-back{left:632px;top:62px;width:143px;height:82px;background:var(--blue);border-color:var(--blue)}
  .card-back .brand{left:0;right:0;top:26px;justify-content:center}
  .card-back .web{position:absolute;left:0;right:0;top:69px;text-align:center;font-size:4px;color:var(--paper)}
  .card-back .band{height:3px;background:var(--orange)}
  .envelope-back{left:472px;top:211px;width:363px;height:156px}
  .envelope-back .flap{position:absolute;left:0;top:0;width:363px;height:50px}
  .envelope-back .seal{position:absolute;left:172px;top:12px;width:20px;height:20px;border-radius:50%;background:var(--orange)}
  .envelope-front{left:472px;top:396px;width:363px;height:156px}
  .envelope-front .brand{left:16px;top:13px}
  .envelope-front .address{position:absolute;left:16px;top:38px;font-size:5px;line-height:1.3}
  .envelope-front .band{height:5px}
  .notepad{left:866px;top:88px;width:293px;height:454px}
  .notepad .brand{left:20px;top:26px}
  .notepad .contact{left:180px;top:20px;font-size:7px}
  .notepad .lines{position:absolute;left:20px;right:20px;top:78px;height:322px;
    background:repeating-linear-gradient(to bottom,transparent 0 15px,var(--rule) 15px 16px)}
  .notepad .band{height:5px}
</style>
</head>
<body>

<section class="sheet letterhead">
  <div class="brand brand-lg"><span class="dot"></span><span class="name"><span>Lumen</span><span>Forge</span></span></div>
  <div class="contact">
    <p>Street Name Avenue, Suite<br>100 State, Zip Code,Country</p>
    <p class="row" style="margin-top:3px"><svg viewBox="0 0 10 10"><path d="M2 1h2l1 2-1 1a5 5 0 0 0 2 2l1-1 2 1v2c0 1-1 1-1 1A7 7 0 0 1 1 2c0 0 0-1 1-1z" fill="var(--blue)"/></svg>410.555.0182</p>
    <p class="row"><svg viewBox="0 0 10 10"><rect x="1" y="2" width="8" height="6" rx="1" fill="var(--blue)"/></svg>info@lumenforge.com</p>
    <p class="row"><svg viewBox="0 0 10 10"><circle cx="5" cy="5" r="4" fill="var(--blue)"/></svg>www.lumenforge.com</p>
  </div>
  <div class="band"></div>
</section>

<section class="sheet card-front">
  <div class="brand brand-sm"><span class="dot"></span><span class="name"><span>Lumen</span><span>Forge</span></span></div>
  <div class="divider"></div>
  <div class="person">
    <p class="who">Dana Whitfield</p>
    <p>President</p>
    <p style="margin-top:3px">Street Name Avenue, Suite<br>100 State, Zip Code,Country</p>
    <p style="margin-top:2px">410.555.0182<br>info@lumenforge.com<br>www.lumenforge.com</p>
  </div>
  <div class="band"></div>
</section>

<section class="sheet card-back">
  <div class="brand brand-sm brand-white"><span class="dot"></span><span class="name"><span>Lumen</span><span>Forge</span></span></div>
  <p class="web">www.lumenforge.com</p>
  <div class="band"></div>
</section>

<section class="sheet envelope-back">
  <svg class="flap" viewBox="0 0 363 50" aria-hidden="true">
    <path d="M0 0 C4 30 8 38 22 38 H341 C355 38 359 30 363 0" fill="none" stroke="var(--edge)" stroke-width="1"/>
  </svg>
  <div class="seal"></div>
</section>

<section class="sheet envelope-front">
  <div class="brand brand-md"><span class="dot"></span><span class="name"><span>Lumen</span><span>Forge</span></span></div>
  <p class="address">Street Name Avenue, Suite<br>100 State, Zip Code,Country</p>
  <div class="band"></div>
</section>

<section class="sheet notepad">
  <div class="brand brand-lg"><span class="dot"></span><span class="name"><span>Lumen</span><span>Forge</span></span></div>
  <div class="contact">
    <p>Street Name Avenue, Suite<br>100 State, Zip Code,Country</p>
    <p class="row" style="margin-top:3px"><svg viewBox="0 0 10 10"><path d="M2 1h2l1 2-1 1a5 5 0 0 0 2 2l1-1 2 1v2c0 1-1 1-1 1A7 7 0 0 1 1 2c0 0 0-1 1-1z" fill="var(--blue)"/></svg>410.555.0182</p>
    <p class="row"><svg viewBox="0 0 10 10"><rect x="1" y="2" width="8" height="6" rx="1" fill="var(--blue)"/></svg>info@lumenforge.com</p>
    <p class="row"><svg viewBox="0 0 10 10"><circle cx="5" cy="5" r="4" fill="var(--blue)"/></svg>www.lumenforge.com</p>
  </div>
  <div class="lines"></div>
  <div class="band"></div>
</section>

</body>
</html>
```